Advertising material for new program

We are launching a new program and need some advertising material.
- Cover photo for facebook (with minimal words on it)
- Social Media graphic (with minimal words on it)
- a5 flyer
- Banner

Information:
- Sensory play is a NEW program at Wren Tumblehall
What is Sensory Play:
*A sensory experience for babies 0 - 13months old.
* Stimulating babies senses
* Engaging movement and balance
- Created by qualified early childhood professional
- starting on Wednesdays in February 2022
- Book online
*www.wrentumblehall.example
-Contact us for more information
*97316258
*info@wrentumblehall.example

NOT INFORMATION FOR THE ADVERTISING
I have attached our style guide, our logo, some material we have done done recently and some photo of my own baby. As its a new program we don't have any photos yet but I am open to ideas

Target Market(s)

Mums aged 25 - 45

Industry/Entity Type

Kids activities

Colors
0054AA
0677BA
7BADD7
CADEEF
E8F1F8
59FF00
82FF00
B8FF75
E3FFCB
F4FFEA

Requirements
Must have
• photos of babies and mums with babies
Should not have
• Photos of adults / teens

```html
<!DOCTYPE html>
<html lang="en">
<head>
<meta charset="utf-8">
<title>Sensory Play – Wren Tumblehall</title>
<link rel="stylesheet" href="https://fonts.googleapis.com/css2?family=Alfa+Slab+One&family=Kaushan+Script&family=Nunito+Sans:wght@300;400&family=Oswald:wght@400;500;600&display=swap">
<style>
  :root {
    --navy: #0c1f45;
    --green: #7ed321;
    --green-bright: #8fdc00;
    --green-dark: #2f6a1f;
    --sensory-ink: #17392f;
    --ink: #1d2533;
    --white: #ffffff;
    --silver: #d9d9d9;
    --ring-grey: #e6e6e6;
  }
  * { margin: 0; padding: 0; box-sizing: border-box; }
  html, body { width: 846px; height: 1200px; overflow: hidden; background: var(--white); }
  .flyer { position: relative; width: 846px; height: 1200px; overflow: hidden; background: var(--white); }
  .backdrop { position: absolute; inset: 0; }

  .brand-name {
    position: absolute; left: 20px; top: 48px; width: 200px;
    font-family: "Oswald", sans-serif; font-weight: 600; font-size: 32px; line-height: 1.05;
    color: var(--green); text-transform: uppercase; letter-spacing: 1px;
  }

  .tagline {
    position: absolute; left: 488px; top: 30px;
    font-family: "Kaushan Script", cursive; font-size: 52px; line-height: 64px;
    color: var(--green); white-space: nowrap;
  }
  .start-band {
    position: absolute; left: 400px; top: 119px; width: 446px; height: 42px;
    background: linear-gradient(90deg, rgba(12,31,69,0) 0%, var(--navy) 16%, var(--navy) 100%);
  }
  .start-line {
    position: absolute; right: 21px; top: 119px;
    font-family: "Oswald", sans-serif; font-weight: 400; font-size: 37px; line-height: 42px;
    color: var(--white); white-space: nowrap; letter-spacing: -0.4px;
  }
  .start-date {
    position: absolute; right: 20px; top: 172px;
    font-family: "Alfa Slab One", serif; font-size: 46px; line-height: 56px; color: var(--silver);
    -webkit-text-stroke: 2px var(--navy); paint-order: stroke fill; white-space: nowrap;
  }
  .title {
    position: absolute; right: 26px;
    font-family: "Alfa Slab One", serif; line-height: 1; white-space: nowrap; letter-spacing: 0;
    -webkit-text-stroke: 4px var(--navy); paint-order: stroke fill;
    text-shadow: 3px 0 0 var(--white), -3px 0 0 var(--white), 0 3px 0 var(--white), 0 -3px 0 var(--white),
                 3px 3px 0 var(--white), -3px -3px 0 var(--white), 3px -3px 0 var(--white), -3px 3px 0 var(--white);
  }
  .title--sensory { top: 232px; font-size: 72px; color: var(--sensory-ink); }
  .title--play { top: 318px; font-size: 76px; color: var(--green-dark); }

  .photo-small, .photo-large { position: absolute; border-radius: 50%; }
  .photo-small {
    left: 210px; top: 578px; width: 230px; height: 230px;
    background:
      radial-gradient(circle at 78% 22%, rgba(214,196,160,0.9) 0%, rgba(214,196,160,0) 32%),
      radial-gradient(circle at 50% 42%, rgba(196,150,118,0.95) 0%, rgba(196,150,118,0) 38%),
      radial-gradient(circle at 40% 78%, rgba(236,232,226,0.95) 0%, rgba(236,232,226,0) 30%),
      radial-gradient(circle at 85% 70%, rgba(120,140,170,0.7) 0%, rgba(120,140,170,0) 30%),
      linear-gradient(135deg, #3a3440 0%, #6e5646 50%, #4a3c38 100%);
  }
  .photo-large {
    left: 502px; top: 483px; width: 290px; height: 290px;
    background:
      radial-gradient(circle at 40% 38%, rgba(240,214,196,0.9) 0%, rgba(240,214,196,0) 26%),
      radial-gradient(circle at 58% 60%, rgba(250,250,250,0.95) 0%, rgba(250,250,250,0) 30%),
      radial-gradient(circle at 78% 40%, rgba(170,172,176,0.8) 0%, rgba(170,172,176,0) 24%),
      linear-gradient(160deg, #e4dfd8 0%, #d4cdc4 60%, #c4bcb2 100%);
  }

  .feature-icon { position: absolute; width: 104px; height: 104px; }
  .feature-text {
    position: absolute; font-family: "Nunito Sans", sans-serif; font-weight: 300;
    font-size: 25px; line-height: 29px; color: var(--ink); white-space: nowrap;
  }

  .book-online {
    position: absolute; left: 618px; top: 1108px;
    font-family: "Oswald", sans-serif; font-weight: 600; font-size: 38px; line-height: 48px; color: var(--green-bright);
  }
  .contact {
    position: absolute; top: 1160px; height: 30px; display: flex; align-items: center; gap: 14px;
    font-family: "Oswald", sans-serif; font-weight: 400; font-size: 22px; color: var(--green-bright); white-space: nowrap;
  }
  .contact svg { flex: none; }
  .contact--phone { left: 24px; }
  .contact--email { left: 220px; }
  .contact--web { left: 548px; }
</style>
</head>
<body>
<main class="flyer">
  <svg class="backdrop" width="846" height="1200" viewBox="0 0 846 1200">
    <defs>
      <linearGradient id="hero-base" x1="0" y1="0" x2="1" y2="0.6">
        <stop offset="0" stop-color="#7a4e26"/>
        <stop offset="0.35" stop-color="#3e4060"/>
        <stop offset="0.65" stop-color="#2a3f66"/>
        <stop offset="1" stop-color="#4f9a2a"/>
      </linearGradient>
      <radialGradient id="hero-amber" cx="0.08" cy="0.55" r="0.35">
        <stop offset="0" stop-color="#c8902e" stop-opacity="0.85"/>
        <stop offset="1" stop-color="#c8902e" stop-opacity="0"/>
      </radialGradient>
      <radialGradient id="hero-cream" cx="0.38" cy="0.32" r="0.3">
        <stop offset="0" stop-color="#d8c8b4" stop-opacity="0.6"/>
        <stop offset="1" stop-color="#d8c8b4" stop-opacity="0"/>
      </radialGradient>
      <radialGradient id="hero-glow" cx="0.46" cy="0.78" r="0.25">
        <stop offset="0" stop-color="#e8e4ff" stop-opacity="0.75"/>
        <stop offset="0.5" stop-color="#9a7ad0" stop-opacity="0.35"/>
        <stop offset="1" stop-color="#9a7ad0" stop-opacity="0"/>
      </radialGradient>
      <radialGradient id="hero-green" cx="0.95" cy="0.75" r="0.4">
        <stop offset="0" stop-color="#6fbf2e" stop-opacity="0.8"/>
        <stop offset="1" stop-color="#6fbf2e" stop-opacity="0"/>
      </radialGradient>
      <linearGradient id="hero-top" x1="0" y1="0" x2="0" y2="1">
        <stop offset="0" stop-color="#0c1f45" stop-opacity="0.95"/>
        <stop offset="0.3" stop-color="#0c1f45" stop-opacity="0.25"/>
        <stop offset="1" stop-color="#0c1f45" stop-opacity="0"/>
      </linearGradient>
    </defs>
    <g role="img" aria-label="Photo: a mother and her baby playing with glowing sensory light toys">
      <path id="hero-shape" d="M0 0 H846 V640 Q640 690 480 682 Q230 660 0 520 Z" fill="url(#hero-base)"/>
      <path d="M0 0 H846 V640 Q640 690 480 682 Q230 660 0 520 Z" fill="url(#hero-amber)"/>
      <path d="M0 0 H846 V640 Q640 690 480 682 Q230 660 0 520 Z" fill="url(#hero-cream)"/>
      <path d="M0 0 H846 V640 Q640 690 480 682 Q230 660 0 520 Z" fill="url(#hero-glow)"/>
      <path d="M0 0 H846 V640 Q640 690 480 682 Q230 660 0 520 Z" fill="url(#hero-green)"/>
      <path d="M0 0 H846 V640 Q640 690 480 682 Q230 660 0 520 Z" fill="url(#hero-top)"/>
    </g>
    <path d="M0 520 Q230 660 480 682 Q640 690 846 640 V652 Q640 700 480 694 Q220 672 0 540 Z" fill="var(--navy)"/>
    <path d="M700 622 Q780 612 846 600 V612 Q780 624 700 634 Z" fill="var(--green)"/>
    <path d="M0 0 H277 Q240 150 100 159 Q45 162 0 145 Z" fill="var(--green)"/>
    <path d="M0 0 H268 Q232 140 100 151 Q45 153 0 137 Z" fill="var(--navy)"/>
    <circle cx="325" cy="693" r="127" fill="var(--ring-grey)"/>
    <path d="M440 693 A115 115 0 0 1 210 693" fill="none" stroke="var(--green)" stroke-width="9"/>
    <circle cx="647" cy="628" r="161" fill="var(--navy)"/>
    <circle cx="647" cy="628" r="154" fill="var(--white)"/>
    <path d="M0 1100 Q420 1150 846 1052 V1200 H0 Z" fill="var(--green-bright)"/>
    <path d="M0 1112 Q420 1162 846 1066 V1200 H0 Z" fill="var(--navy)"/>
  </svg>

  <div class="brand-name">Wren<br>Tumblehall</div>

  <p class="tagline">Newly lanched!</p>
  <div class="start-band"></div>
  <p class="start-line">STARTING ON WEDNESDAYS IN</p>
  <p class="start-date">FEBRUARY 2022</p>
  <h1 class="title title--sensory">SENSORY</h1>
  <p class="title title--play">PLAY</p>

  <div class="photo-small" role="img" aria-label="Photo: a mum clapping with babies at a group play session"></div>
  <div class="photo-large" role="img" aria-label="Photo: a smiling baby lying on a soft white blanket"></div>

  <svg class="feature-icon" style="left:30px;top:824px" viewBox="0 0 104 104" role="img" aria-label="Heart icon">
    <circle cx="52" cy="52" r="50" fill="var(--ring-grey)"/>
    <circle cx="52" cy="52" r="47" fill="var(--white)" stroke="var(--green)" stroke-width="2.5"/>
    <path d="M52 74 C30 60 24 50 24 41 C24 33 30 28 37 28 C44 28 49 32 52 38 C55 32 60 28 67 28 C74 28 80 33 80 41 C80 50 74 60 52 74 Z"
          fill="none" stroke="var(--green)" stroke-width="2.5" stroke-linejoin="round"/>
  </svg>
  <p class="feature-text" style="left:147px;top:830px">A sensory experience<br>for babies 0-3months<br>old.</p>

  <svg class="feature-icon" style="left:441px;top:824px" viewBox="0 0 104 104" role="img" aria-label="Tick icon">
    <circle cx="52" cy="52" r="50" fill="var(--ring-grey)"/>
    <circle cx="52" cy="52" r="47" fill="var(--white)" stroke="var(--green)" stroke-width="2.5"/>
    <circle cx="52" cy="52" r="27" fill="none" stroke="var(--green)" stroke-width="2.5"/>
    <path d="M39 53 L48 62 L66 43" fill="none" stroke="var(--green)" stroke-width="3" stroke-linecap="round" stroke-linejoin="round"/>
  </svg>
  <p class="feature-text" style="left:552px;top:833px">Created by qualified<br>early childhood<br>professional.</p>

  <svg class="feature-icon" style="left:30px;top:968px" viewBox="0 0 104 104" role="img" aria-label="Stacked blocks icon">
    <circle cx="52" cy="52" r="50" fill="var(--ring-grey)"/>
    <circle cx="52" cy="52" r="47" fill="var(--white)" stroke="var(--green)" stroke-width="2.5"/>
    <g fill="none" stroke="var(--green)" stroke-width="2.2">
      <rect x="42" y="24" width="20" height="18" rx="2"/>
      <rect x="32" y="42" width="20" height="18" rx="2"/>
      <rect x="52" y="42" width="20" height="18" rx="2"/>
      <rect x="22" y="60" width="20" height="18" rx="2"/>
      <rect x="42" y="60" width="20" height="18" rx="2"/>
      <rect x="62" y="60" width="20" height="18" rx="2"/>
    </g>
  </svg>
  <p class="feature-text" style="left:147px;top:991px">Engaging movement &amp;<br>balance</p>

  <svg class="feature-icon" style="left:441px;top:965px" viewBox="0 0 104 104" role="img" aria-label="Senses network icon">
    <circle cx="52" cy="52" r="50" fill="var(--ring-grey)"/>
    <circle cx="52" cy="52" r="47" fill="var(--white)" stroke="var(--green)" stroke-width="2.5"/>
    <g fill="none" stroke="var(--green)" stroke-width="2.5" stroke-linecap="round">
      <circle cx="52" cy="26" r="4"/><path d="M52 30 V80"/>
      <circle cx="38" cy="36" r="4"/><path d="M38 40 V50 L44 56 V80"/>
      <circle cx="66" cy="36" r="4"/><path d="M66 40 V50 L60 56 V80"/>
      <circle cx="26" cy="52" r="4"/><path d="M26 56 V62 L32 68 V80"/>
      <circle cx="78" cy="52" r="4"/><path d="M78 56 V62 L72 68 V80"/>
    </g>
  </svg>
  <p class="feature-text" style="left:557px;top:982px">Stimulating babies<br>senses</p>

  <p class="book-online">Book online</p>

  <div class="contact contact--phone">
    <svg width="32" height="30" viewBox="0 0 32 30" fill="none" stroke="var(--green-bright)" stroke-width="1.6">
      <rect x="9" y="2" width="14" height="26" rx="2"/><path d="M13 24 H19"/>
      <path d="M5 8 Q3 11 5 14 M27 8 Q29 11 27 14"/>
    </svg>
    <span>97316258</span>
  </div>
  <div class="contact contact--email">
    <svg width="30" height="22" viewBox="0 0 30 22" fill="none" stroke="var(--green-bright)" stroke-width="1.8">
      <rect x="1" y="1" width="28" height="20" rx="1"/><path d="M1 2 L15 13 L29 2"/>
    </svg>
    <span>info@wrentumblehall.example</span>
  </div>
  <div class="contact contact--web">
    <svg width="26" height="26" viewBox="0 0 26 26" fill="none" stroke="var(--green-bright)" stroke-width="1.4">
      <circle cx="13" cy="13" r="11"/><ellipse cx="13" cy="13" rx="5" ry="11"/>
      <path d="M2 13 H24 M4 7 H22 M4 19 H22"/>
    </svg>
    <span>www.wrentumblehall.example</span>
  </div>
</main>
</body>
</html>
```